Book cover for a New Adult, romance/ contemporary novel.

I need a full front, back, and spine cover for my upcoming book. The novel is a romance/ coming of age book and is similar to Every Quiet Harbor by Marissa Colfax. My main audience is women in their late teens/ early 20's. The book is an emotional, reminiscent piece and I would love to see some cover designs with a darker palette like Waiting on Belmora, Nine Rooms Between, or Bartholomew and Kip (but I also adore some lighter covers, especially those that feature the couple such as A Different Then or Past Each Hour). Feel free to send some minimal designs as well if you have any! A great idea of that would be the cover for Salt and Clover or Waiting on Belmora. If you go with a minimal design, I'd love to see silhouettes or maybe a burning candle. Another possible idea I thought of would be a scene at a concert with the crowd silhouetted and then my main character (more details on her below) standing in the middle of it all. I prefer animation/drawing etc over real models. But feel free to send me whatever you think might match the vibe, I'd love to see anything you have in mind! Some main symbols in my book are stars and candles. The main character (Marisol) is a female Korean with brown, medium length straight hair, and the love interest (Theo) is a tall and thin male Caucasian with curly brown hair. The book is openly emotional, wistful, and sets an ache in your chest, so I can't wait to see what designs you artists come up with! (My barcode will need to be included on the back cover, and I am getting that soon!)
The title is "The Weight of Daylight" and the author's name is Brenna Quill. The book's dimensions will be 5.5x8.25. The blurb for the back cover is:
When happily ever falls apart, all you can do is move forward… and reminisce. Marisol Ahn returns home from college following a tragic incident she can’t bring herself to talk about and a breakup with her boyfriend, Theo Marsh. Finding it difficult to confront her traumas, she begins therapy. Marisol takes the therapist on a rollercoaster journey of her college life, retelling the events that caused her relationship to spiral out of control and led to her dropping out of pre-med despite that being her life-long dream. Marisol sets out to remember how things were before everything got so messed up, and figure out how to continue living now that they are.
The author bio for the back cover is:
Brenna Quill is the author of The Restless and Bold. She is a self published writer from Las Vegas who likes to pretend she’s currently in a New York bookstore, drinking a latte, while listening to a carefully curated playlist. When she’s not writing, Brenna is taking care of her plant babies and cuddling with the cutest puppy in the world.

```html
<!DOCTYPE html>
<html lang="en">
<head>
<meta charset="utf-8">
<title>The Weight of Daylight — Full Cover</title>
<link rel="stylesheet" href="https://fonts.googleapis.com/css2?family=Marcellus+SC&family=Shadows+Into+Light+Two&family=Merriweather:wght@300&display=swap">
<style>
  :root {
    --page: #ffffff;
    --night: #0f2a66;
    --night-deep: #0b2257;
    --seam: #0a1f50;
    --ink-light: #f6f3ec;
    --star: #ffffff;
    --star-glow: rgba(190, 215, 255, 0.75);
    --figure-glow: rgba(170, 200, 255, 0.32);
    --barcode-box: #ffffff;
  }
  * { box-sizing: border-box; margin: 0; padding: 0; }
  html, body {
    width: 1200px; height: 1200px; overflow: hidden;
    background: var(--page);
  }
  .canvas { position: relative; width: 1200px; height: 1200px; }
  .cover-spread {
    position: absolute; left: 182px; top: 302px;
    width: 835px; height: 596px;
    display: flex;
    background: var(--night);
    color: var(--ink-light);
  }
  .back-cover { position: relative; width: 398px; height: 100%; }
  .spine {
    position: relative; width: 36px; height: 100%;
    border-left: 1px solid var(--seam);
    border-right: 1px solid var(--seam);
  }
  .front-cover { position: relative; width: 401px; height: 100%; overflow: hidden; }

  .starfield { position: absolute; inset: 0; pointer-events: none; }
  .star {
    position: absolute; width: 4px; height: 4px; margin: -2px 0 0 -2px;
    border-radius: 50%;
    background: var(--star);
    box-shadow: 0 0 6px 3px var(--star-glow), 0 0 14px 5px rgba(150, 190, 255, 0.25);
  }
  .star.small { width: 3px; height: 3px; box-shadow: 0 0 4px 2px var(--star-glow); }

  .title {
    font-family: "Marcellus SC", serif;
    font-weight: 400;
    line-height: 1;
    white-space: nowrap;
    text-shadow: 0 2px 3px rgba(0,0,0,0.35);
  }
  .title .small { font-size: 0.72em; }

  .back-title {
    position: absolute; top: 42px; left: 0; width: 100%;
    text-align: center; font-size: 34px;
  }
  .back-title .line-one { display: block; margin-left: -30px; }
  .back-title .line-two { display: block; margin-top: 14px; margin-left: 30px; }

  .blurb {
    position: absolute; top: 180px; left: 38px; width: 330px;
    font-family: "Shadows Into Light Two", cursive;
    font-size: 13.4px; line-height: 19.2px;
    text-align: center;
  }

  .author-bio {
    position: absolute; top: 422px; left: 30px; width: 186px;
    font-family: "Merriweather", serif; font-weight: 300;
    font-size: 9.6px; line-height: 12.2px;
  }

  .barcode-area {
    position: absolute; left: 245px; top: 488px;
    width: 129px; height: 81px;
    background: var(--barcode-box);
  }

  .spine-title, .spine-author {
    position: absolute; left: 50%;
    writing-mode: vertical-rl;
    transform: translateX(-50%);
    white-space: nowrap;
  }
  .spine-title { top: 24px; font-size: 19px; }
  .spine-author {
    top: 415px;
    font-family: "Shadows Into Light Two", cursive;
    font-size: 21px;
  }

  .couple-art {
    position: absolute; left: 12px; top: 334px;
    width: 376px; height: 262px;
    border-radius: 48% 48% 0 0 / 40% 40% 0 0;
    background:
      radial-gradient(ellipse 60% 70% at 40% 60%, var(--figure-glow), transparent 70%),
      radial-gradient(ellipse 55% 75% at 68% 50%, var(--figure-glow), transparent 70%),
      linear-gradient(180deg, var(--night) 0%, var(--night-deep) 100%);
  }

  .front-title {
    position: absolute; top: 46px; left: 22px; font-size: 50px;
  }
  .front-title .line-one { display: block; }
  .front-title .line-two { display: block; margin-top: 58px; margin-left: 8px; }

  .front-author {
    position: absolute; top: 512px; left: 0; width: 100%;
    text-align: center;
    font-family: "Shadows Into Light Two", cursive;
    font-size: 52px; line-height: 1;
    text-shadow: 0 2px 3px rgba(0,0,0,0.4);
  }
</style>
</head>
<body>
<main class="canvas">
  <section class="cover-spread">
    <article class="back-cover">
      <div class="starfield" aria-hidden="true">
        <span class="star" style="left:87px;top:44px"></span>
        <span class="star" style="left:264px;top:47px"></span>
        <span class="star" style="left:69px;top:113px"></span>
        <span class="star" style="left:345px;top:81px"></span>
        <span class="star small" style="left:290px;top:97px"></span>
        <span class="star" style="left:115px;top:166px"></span>
        <span class="star" style="left:317px;top:161px"></span>
        <span class="star small" style="left:364px;top:13px"></span>
        <span class="star small" style="left:240px;top:144px"></span>
        <span class="star" style="left:331px;top:411px"></span>
        <span class="star small" style="left:237px;top:446px"></span>
      </div>
      <h2 class="title back-title">
        <span class="line-one"><span class="small">The</span> Weight</span>
        <span class="line-two"><span class="small">of</span> Daylight</span>
      </h2>
      <p class="blurb">When happily ever falls apart, all you can do is move forward… and reminisce. Marisol Ahn returns home from college following a tragic incident she can’t bring herself to talk about and a breakup with her boyfriend, Theo Marsh. Finding it difficult to confront her traumas, she begins therapy. Marisol takes the therapist on a rollercoaster journey of her college life, retelling the events that caused her relationship to spiral out of control and led to her dropping out of pre-med despite that being her life-long dream. Marisol sets out to remember how things were before everything got so messed up, and figure out how to continue living now that they are.</p>
      <p class="author-bio">Brenna Quill is the author of The Restless and Bold. She is a self published writer from Las Vegas who likes to pretend she’s currently in a New York bookstore, drinking a latte, while listening to a carefully curated playlist. When she’s not writing, Brenna is taking care of her plant babies and cuddling with the cutest puppy in the world.</p>
      <div class="barcode-area" aria-label="Space reserved for barcode"></div>
    </article>

    <aside class="spine">
      <span class="title spine-title"><span class="small">The</span> Weight <span class="small">of</span> Daylight</span>
      <span class="spine-author">Brenna Quill</span>
    </aside>

    <article class="front-cover">
      <div class="couple-art" role="img" aria-label="Glowing white line illustration of a couple in silhouette, foreheads nearly touching, against a starry night sky"></div>
      <div class="starfield" aria-hidden="true">
        <span class="star" style="left:51px;top:26px"></span>
        <span class="star small" style="left:168px;top:22px"></span>
        <span class="star" style="left:55px;top:144px"></span>
        <span class="star" style="left:230px;top:119px"></span>
        <span class="star small" style="left:263px;top:134px"></span>
        <span class="star small" style="left:218px;top:153px"></span>
        <span class="star" style="left:358px;top:283px"></span>
        <span class="star" style="left:161px;top:303px"></span>
        <span class="star small" style="left:333px;top:314px"></span>
        <span class="star" style="left:58px;top:344px"></span>
        <span class="star small" style="left:155px;top:345px"></span>
        <span class="star" style="left:368px;top:406px"></span>
      </div>
      <h1 class="title front-title">
        <span class="line-one"><span class="small">The</span> Weight</span>
        <span class="line-two"><span class="small">of</span> Daylight</span>
      </h1>
      <p class="front-author">Brenna Quill</p>
    </article>
  </section>
</main>
</body>
</html>
```